Need design for an App.

The app in question is related to security and crime events with real time feed, engagement with friends and posting pictures, we want a sleak, minimal style. There are 11 or 12 screens to be made. We are adding video file as suggestion. We are not sure about colors so we accept suggestions. We are also adding the logo.

Reason: Just giving more time to designers. Thanks.

Industry/Entity Type

Security

Font styles to use
Sans Serif

Requirements
Must have
• The app must have a Login view; a new user view (with nickname, email and pass); a retrieve pass view; a menu view with options for alert configuration, send emergency alert and send report, a feed view with the most popular reports (3 worldwide at the top and near reports after), a profile view with avatar and personal reports, a send emergency alert view with a camera view; a configuration view when the user can put up to 5 contacts to send the alert to them;a send report view with camera and options to configure the camera; a edit report view where the user can see the 3 photos he will update and add a comment of those photos.
Nice to have
• Check the files we are open minds
Should not have
• old design

```html
<!DOCTYPE html>
<html lang="en">
<head>
<meta charset="utf-8">
<title>Vigila – App Screens</title>
<link href="https://fonts.googleapis.com/css2?family=Roboto:wght@400;500;700&display=swap" rel="stylesheet">
<style>
  :root {
    --brand-red: #c8283f;
    --brand-red-soft: #f8dfe2;
    --ink: #222222;
    --muted: #555555;
    --faint: #b5b5b5;
    --field: #e6e6e6;
    --field-text: #a8a8a8;
    --tabbar: #dcdcdc;
    --tab-active: #e9e9e9;
    --icon-grey: #6d6d6d;
    --page-bg: #f2f2f2;
    --screen-bg: #ffffff;
    --divider: #e2e2e2;
    --dark-button: #2e2e2e;
  }
  * { box-sizing: border-box; margin: 0; padding: 0; }
  html, body {
    width: 1200px; height: 675px; overflow: hidden;
    background: var(--page-bg);
    font-family: "Roboto", Arial, sans-serif;
    color: var(--ink);
  }
  .canvas { position: relative; width: 1200px; height: 675px; }

  .screen {
    position: absolute; top: 132px; width: 230px; height: 410px;
    background: var(--screen-bg);
    display: flex; flex-direction: column; overflow: hidden;
    box-shadow: 0 2px 10px rgba(0,0,0,.12);
  }
  .screen--register { left: 44px; }
  .screen--report { left: 348px; }
  .screen--trending { left: 644px; }
  .screen--account { left: 934px; }

  .status-bar {
    height: 15px; flex: none; display: flex; align-items: center;
    justify-content: space-between; padding: 0 6px;
    font-size: 7px; color: var(--ink); background: var(--screen-bg);
  }
  .status-bar__carrier { display: flex; align-items: center; gap: 3px; }
  .status-bar__battery { display: flex; align-items: center; gap: 3px; }

  .app-header {
    height: 34px; flex: none; background: var(--brand-red);
    color: #fff; font-size: 12px; font-weight: 500;
    display: flex; align-items: center; justify-content: center; position: relative;
  }
  .app-header__action { position: absolute; right: 10px; top: 9px; }

  .screen-body { flex: 1; position: relative; overflow: hidden; }

  .tab-bar {
    height: 40px; flex: none; background: var(--tabbar);
    display: flex;
  }
  .tab {
    flex: 1; display: flex; flex-direction: column; align-items: center;
    justify-content: center; gap: 2px; font-size: 5.5px; color: var(--muted);
    border-top: 2px solid transparent;
  }
  .tab--active { background: var(--tab-active); border-top-color: var(--brand-red); }

  /* Register */
  .register { display: flex; flex-direction: column; align-items: center; padding-top: 14px; }
  .brand-name { font-size: 26px; font-weight: 400; color: var(--brand-red); letter-spacing: 1px; line-height: 1; }
  .register__welcome { font-size: 9px; margin-top: 6px; }
  .register__title { font-size: 11px; font-weight: 500; margin-top: 1px; }
  .avatar-ring {
    width: 60px; height: 60px; border-radius: 50%;
    border: 1.5px solid var(--brand-red); background: var(--field);
    display: flex; align-items: center; justify-content: center; overflow: hidden;
  }
  .register .avatar-ring { margin-top: 10px; }
  .form { display: flex; flex-direction: column; gap: 8px; margin-top: 14px; }
  .field {
    width: 182px; height: 30px; background: var(--field);
    font-size: 9px; color: var(--field-text); padding-left: 7px;
    display: flex; align-items: center;
  }
  .register__button {
    margin-top: 17px; width: 160px; height: 31px; background: var(--brand-red);
    color: #fff; font-size: 9px; display: flex; align-items: center; justify-content: center;
  }
  .register__help { margin-top: 26px; font-size: 8px; font-weight: 500; }

  /* Report */
  .report-draft { padding: 25px 10px 12px; border-bottom: 1px solid var(--divider); box-shadow: 0 1px 2px rgba(0,0,0,.06); }
  .photo-strip { display: flex; justify-content: center; gap: 4px; }
  .photo {
    width: 40px; height: 52px;
  }
  .photo--park { background: linear-gradient(160deg, #9aa08a, #5d6150 70%, #b5b3a5); }
  .photo--autumn { background: linear-gradient(160deg, #c79a35, #8a6a22 60%, #d8b55c); }
  .caption { font-size: 5.8px; line-height: 1.35; color: var(--muted); text-align: center; margin: 6px 18px 0; }
  .upload { display: flex; flex-direction: column; align-items: center; padding-top: 22px; }
  .upload__label { font-size: 7px; color: var(--faint); margin-top: 4px; }
  .upload .caption { color: #c9c9c9; margin-top: 4px; }
  .ad-banner {
    position: absolute; left: 12px; bottom: 10px; width: 206px; height: 50px;
    background: linear-gradient(100deg, #6fae3a, #4a8ed8 45%, #b9d97a);
    border: 1px solid #d0d0d0;
  }
  .ad-banner__close {
    position: absolute; right: -6px; top: -7px; width: 13px; height: 13px;
    border-radius: 50%; background: #e0262f; border: 1.5px solid #fff;
  }

  /* Trending */
  .segment {
    margin: 9px auto 8px; width: 162px; height: 20px;
    border: 1px solid var(--brand-red); border-radius: 10px; display: flex; overflow: hidden;
    font-size: 7px;
  }
  .segment__option { flex: 1; display: flex; align-items: center; justify-content: center; color: var(--brand-red); }
  .segment__option--active { background: var(--brand-red); color: #fff; border-radius: 10px; }
  .feed { border-top: 1px solid var(--divider); }
  .feed-item {
    display: flex; gap: 6px; padding: 6px 8px 7px; border-bottom: 1px solid #ecc5ca;
    position: relative; height: 45px;
  }
  .feed-item--popular { background: var(--brand-red-soft); }
  .feed-item--near { border-bottom-color: var(--divider); }
  .feed-avatar { width: 30px; height: 30px; border-radius: 50%; flex: none; background: #c9a58f; border: 1px solid #fff; }
  .feed-avatar--b { background: #8fa3b5; }
  .feed-avatar--c { background: #b08d7a; }
  .feed-avatar--d { background: #a5a29c; }
  .feed-avatar--e { background: #9c9a98; }
  .feed-item__name { font-size: 6.5px; color: var(--brand-red); }
  .feed-item__text { font-size: 5.3px; line-height: 1.3; color: var(--muted); margin-top: 1px; width: 150px; }
  .feed-item__time { position: absolute; right: 8px; top: 13px; font-size: 4.8px; color: var(--muted); }

  /* Account */
  .account-rows { position: absolute; left: 0; right: 0; top: 0; }
  .account-rows div { height: 38px; border-bottom: 1px solid var(--divider); }
  .account .avatar-ring { position: absolute; left: 14px; top: 20px; width: 60px; height: 60px; }
  .modal {
    position: absolute; left: 12px; top: 72px; width: 210px; height: 206px;
    background: #fff; box-shadow: 0 1px 6px rgba(0,0,0,.18);
    display: flex; flex-direction: column; align-items: center; padding-top: 10px;
  }
  .modal__title { font-size: 8.5px; font-weight: 500; }
  .modal .form { margin-top: 12px; gap: 8px; }
  .modal .field { width: 182px; }
  .modal__button {
    margin-top: 17px; width: 190px; height: 30px; background: var(--dark-button);
    color: #fff; font-size: 9px; font-weight: 500; display: flex; align-items: center; justify-content: center;
  }
  .emergency-button {
    position: absolute; left: 18px; top: 282px; width: 190px; height: 28px; background: var(--brand-red);
    color: #fff; font-size: 8.5px; font-weight: 500; display: flex; align-items: center; justify-content: center;
  }
</style>
</head>
<body>
<div class="canvas">

  <!-- Registration -->
  <section class="screen screen--register">
    <div class="status-bar">
      <span class="status-bar__carrier">●●●○○ NOVA
        <svg width="8" height="6" viewBox="0 0 8 6"><path d="M0 2a6 6 0 0 1 8 0M1.5 3.5a4 4 0 0 1 5 0M3 5a2 2 0 0 1 2 0" stroke="#222" fill="none" stroke-width=".8"/></svg></span>
      <span>4:21 PM</span>
      <span class="status-bar__battery">22%
        <svg width="14" height="6" viewBox="0 0 14 6"><rect x=".4" y=".4" width="12" height="5.2" fill="none" stroke="#222" stroke-width=".8"/><rect x="1.2" y="1.2" width="3" height="3.6" fill="#222"/><rect x="12.6" y="2" width="1.2" height="2" fill="#222"/></svg></span>
    </div>
    <div class="screen-body register">
      <div class="brand-name">Vigila</div>
      <div class="register__welcome">Welcome to Vigila</div>
      <div class="register__title">Registration</div>
      <div class="avatar-ring">
        <svg width="58" height="58" viewBox="0 0 58 58"><circle cx="29" cy="22" r="11" fill="#fff"/><path d="M8 58a21 19 0 0 1 42 0z" fill="#fff"/><rect x="22" y="18" width="14" height="10" rx="1.5" fill="#777"/><circle cx="29" cy="23" r="3" fill="#fff"/></svg>
      </div>
      <div class="form">
        <div class="field">nickname</div>
        <div class="field">mail id</div>
        <div class="field">password</div>
        <div class="field">confirm password</div>
      </div>
      <div class="register__button">Register</div>
      <div class="register__help">Need help?</div>
    </div>
  </section>

  <!-- Report -->
  <section class="screen screen--report">
    <div class="status-bar">
      <span class="status-bar__carrier">●●●○○ NOVA
        <svg width="8" height="6" viewBox="0 0 8 6"><path d="M0 2a6 6 0 0 1 8 0M1.5 3.5a4 4 0 0 1 5 0M3 5a2 2 0 0 1 2 0" stroke="#222" fill="none" stroke-width=".8"/></svg></span>
      <span>4:21 PM</span>
      <span class="status-bar__battery">22%
        <svg width="14" height="6" viewBox="0 0 14 6"><rect x=".4" y=".4" width="12" height="5.2" fill="none" stroke="#222" stroke-width=".8"/><rect x="1.2" y="1.2" width="3" height="3.6" fill="#222"/><rect x="12.6" y="2" width="1.2" height="2" fill="#222"/></svg></span>
    </div>
    <header class="app-header">Report</header>
    <div class="screen-body">
      <div class="report-draft">
        <div class="photo-strip">
          <div class="photo photo--park" role="img" aria-label="Report photo of a person in a park"></div>
          <div class="photo photo--autumn" role="img" aria-label="Report photo of a person among autumn leaves"></div>
          <div class="photo photo--park" role="img" aria-label="Report photo of a person in a park"></div>
          <div class="photo photo--autumn" role="img" aria-label="Report photo of a person among autumn leaves"></div>
        </div>
        <p class="caption">This is Drafto's version of Lorem Ipsum. Proin gravida nibh vel velit auctor aliquet. Aenean sollicitudin, lorem quis bibendum auctor, nisi elit consequat ipsum,</p>
      </div>
      <div class="upload">
        <svg width="80" height="64" viewBox="0 0 80 64"><rect x="2" y="10" width="76" height="52" rx="3" fill="#c9c9c9"/><rect x="52" y="3" width="18" height="9" rx="1.5" fill="#c9c9c9"/><circle cx="38" cy="36" r="20" fill="#fff"/><circle cx="38" cy="36" r="14" fill="#c9c9c9"/><path d="M30 33a9 9 0 0 1 9-8" stroke="#fff" stroke-width="3" fill="none" stroke-linecap="round"/></svg>
        <div class="upload__label">Upload Photos</div>
        <p class="caption">This is Drafto's version of Lorem Ipsum. Proin gravida nibh vel velit auctor aliquet. Aenean sollicitudin, lorem quis bibendum</p>
      </div>
      <div class="ad-banner" role="img" aria-label="Advertising banner with a cartoon game illustration">
        <span class="ad-banner__close"></span>
      </div>
    </div>
    <nav class="tab-bar">
      <div class="tab tab--active"><svg width="18" height="14" viewBox="0 0 18 14"><rect x="1" y="2" width="16" height="11" rx="1.5" fill="#6d6d6d"/><circle cx="9" cy="7.5" r="3.5" fill="#fff"/><circle cx="9" cy="7.5" r="2" fill="#6d6d6d"/></svg>Report</div>
      <div class="tab"><svg width="18" height="14" viewBox="0 0 18 14"><rect x="2" y="9" width="2.5" height="4" fill="#6d6d6d"/><rect x="6" y="7" width="2.5" height="6" fill="#6d6d6d"/><rect x="10" y="4" width="2.5" height="9" fill="#6d6d6d"/><rect x="14" y="1" width="2.5" height="12" fill="#6d6d6d"/></svg>Trending</div>
      <div class="tab"><svg width="14" height="14" viewBox="0 0 14 14"><circle cx="7" cy="7" r="6.5" fill="#6d6d6d"/><path d="M7 3v4h3" stroke="#fff" stroke-width="1.2" fill="none"/></svg>Time Line</div>
      <div class="tab"><svg width="14" height="14" viewBox="0 0 14 14"><circle cx="7" cy="4" r="3.5" fill="#6d6d6d"/><path d="M0 14a7 6 0 0 1 14 0z" fill="#6d6d6d"/></svg>Account</div>
    </nav>
  </section>

  <!-- Trending -->
  <section class="screen screen--trending">
    <div class="status-bar">
      <span class="status-bar__carrier">●●●○○ NOVA
        <svg width="8" height="6" viewBox="0 0 8 6"><path d="M0 2a6 6 0 0 1 8 0M1.5 3.5a4 4 0 0 1 5 0M3 5a2 2 0 0 1 2 0" stroke="#222" fill="none" stroke-width=".8"/></svg></span>
      <span>4:21 PM</span>
      <span class="status-bar__battery">22%
        <svg width="14" height="6" viewBox="0 0 14 6"><rect x=".4" y=".4" width="12" height="5.2" fill="none" stroke="#222" stroke-width=".8"/><rect x="1.2" y="1.2" width="3" height="3.6" fill="#222"/><rect x="12.6" y="2" width="1.2" height="2" fill="#222"/></svg></span>
    </div>
    <header class="app-header">Trending
      <svg class="app-header__action" width="14" height="14" viewBox="0 0 14 14"><circle cx="6" cy="6" r="4.8" stroke="#fff" stroke-width="1.2" fill="none"/><path d="M9.5 9.5L13 13" stroke="#fff" stroke-width="1.3"/></svg>
    </header>
    <div class="screen-body">
      <div class="segment">
        <div class="segment__option">Most Popular</div>
        <div class="segment__option segment__option--active">Near</div>
      </div>
      <div class="feed">
        <article class="feed-item feed-item--popular">
          <div class="feed-avatar" role="img" aria-label="Profile photo of Andera"></div>
          <div><div class="feed-item__name">Andera</div><p class="feed-item__text">This is Drafto's version of Lorem Ipsum. Proin gravida nibh vel velit auctor aliquet. Aenean sollicitudin, lorem quis bibendum auctor, nisi elit consequat ipsum, nec sagittis sem nibh id elit.</p></div>
          <span class="feed-item__time">10:30</span>
        </article>
        <article class="feed-item feed-item--popular">
          <div class="feed-avatar feed-avatar--b" role="img" aria-label="Profile photo of Jhon"></div>
          <div><div class="feed-item__name">Jhon</div><p class="feed-item__text">This is Drafto's version of Lorem Ipsum. Proin gravida nibh vel velit auctor aliquet. Aenean sollicitudin, lorem quis bibendum auctor, nisi elit consequat ipsum, nec sagittis sem nibh id elit.</p></div>
          <span class="feed-item__time">09:37</span>
        </article>
        <article class="feed-item feed-item--popular">
          <div class="feed-avatar feed-avatar--c" role="img" aria-label="Profile photo of Kelly"></div>
          <div><div class="feed-item__name">Kelly</div><p class="feed-item__text">This is Drafto's version of Lorem Ipsum. Proin gravida nibh vel velit auctor aliquet. Aenean sollicitudin, lorem quis bibendum auctor, nisi elit consequat ipsum, nec sagittis sem nibh id elit.</p></div>
          <span class="feed-item__time">09:10</span>
        </article>
        <article class="feed-item feed-item--near">
          <div class="feed-avatar feed-avatar--d" role="img" aria-label="Profile photo of Peter"></div>
          <div><div class="feed-item__name">Peter</div><p class="feed-item__text">This is Drafto's version of Lorem Ipsum. Proin gravida nibh vel velit auctor aliquet. Aenean sollicitudin, lorem quis bibendum auctor, nisi elit consequat ipsum, nec sagittis sem nibh id elit.</p></div>
          <span class="feed-item__time">08:42</span>
        </article>
        <article class="feed-item feed-item--near">
          <div class="feed-avatar feed-avatar--e" role="img" aria-label="Profile photo of Kim"></div>
          <div><div class="feed-item__name">Kim</div><p class="feed-item__text">This is Drafto's version of Lorem Ipsum. Proin gravida nibh vel velit auctor aliquet. Aenean sollicitudin, lorem quis bibendum auctor, nisi elit consequat ipsum, nec sagittis sem nibh id elit.</p></div>
          <span class="feed-item__time">08:22</span>
        </article>
      </div>
    </div>
    <nav class="tab-bar">
      <div class="tab"><svg width="18" height="14" viewBox="0 0 18 14"><rect x="1" y="2" width="16" height="11" rx="1.5" fill="#6d6d6d"/><circle cx="9" cy="7.5" r="3.5" fill="#fff"/><circle cx="9" cy="7.5" r="2" fill="#6d6d6d"/></svg>Report</div>
      <div class="tab tab--active"><svg width="18" height="14" viewBox="0 0 18 14"><rect x="2" y="9" width="2.5" height="4" fill="#6d6d6d"/><rect x="6" y="7" width="2.5" height="6" fill="#6d6d6d"/><rect x="10" y="4" width="2.5" height="9" fill="#6d6d6d"/><rect x="14" y="1" width="2.5" height="12" fill="#6d6d6d"/></svg>Trending</div>
      <div class="tab"><svg width="14" height="14" viewBox="0 0 14 14"><circle cx="7" cy="7" r="6.5" fill="#6d6d6d"/><path d="M7 3v4h3" stroke="#fff" stroke-width="1.2" fill="none"/></svg>Time Line</div>
      <div class="tab"><svg width="14" height="14" viewBox="0 0 14 14"><circle cx="7" cy="4" r="3.5" fill="#6d6d6d"/><path d="M0 14a7 6 0 0 1 14 0z" fill="#6d6d6d"/></svg>Account</div>
    </nav>
  </section>

  <!-- Account -->
  <section class="screen screen--account">
    <div class="status-bar">
      <span class="status-bar__carrier">●●●○○ NOVA
        <svg width="8" height="6" viewBox="0 0 8 6"><path d="M0 2a6 6 0 0 1 8 0M1.5 3.5a4 4 0 0 1 5 0M3 5a2 2 0 0 1 2 0" stroke="#222" fill="none" stroke-width=".8"/></svg></span>
      <span>4:21 PM</span>
      <span class="status-bar__battery">22%
        <svg width="14" height="6" viewBox="0 0 14 6"><rect x=".4" y=".4" width="12" height="5.2" fill="none" stroke="#222" stroke-width=".8"/><rect x="1.2" y="1.2" width="3" height="3.6" fill="#222"/><rect x="12.6" y="2" width="1.2" height="2" fill="#222"/></svg></span>
    </div>
    <header class="app-header">Account
      <svg class="app-header__action" width="14" height="14" viewBox="0 0 14 14"><path d="M2 12l1-3.5L10.5 1l2.5 2.5L5.5 11z" stroke="#fff" stroke-width="1" fill="none"/><path d="M1 13.2h5" stroke="#fff" stroke-width="1"/></svg>
    </header>
    <div class="screen-body account">
      <div class="account-rows"><div></div><div></div><div></div><div></div><div></div><div></div><div></div><div></div></div>
      <div class="avatar-ring">
        <svg width="58" height="58" viewBox="0 0 58 58"><circle cx="29" cy="22" r="11" fill="#fff"/><path d="M8 58a21 19 0 0 1 42 0z" fill="#fff"/></svg>
      </div>
      <div class="modal">
        <div class="modal__title">Change Password</div>
        <div class="form">
          <div class="field">old password</div>
          <div class="field">new password</div>
          <div class="field">confirm password</div>
        </div>
        <div class="modal__button">Update</div>
      </div>
      <div class="emergency-button">Emergency Contact Numbers</div>
    </div>
    <nav class="tab-bar">
      <div class="tab"><svg width="18" height="14" viewBox="0 0 18 14"><rect x="1" y="2" width="16" height="11" rx="1.5" fill="#6d6d6d"/><circle cx="9" cy="7.5" r="3.5" fill="#fff"/><circle cx="9" cy="7.5" r="2" fill="#6d6d6d"/></svg>Report</div>
      <div class="tab"><svg width="18" height="14" viewBox="0 0 18 14"><rect x="2" y="9" width="2.5" height="4" fill="#6d6d6d"/><rect x="6" y="7" width="2.5" height="6" fill="#6d6d6d"/><rect x="10" y="4" width="2.5" height="9" fill="#6d6d6d"/><rect x="14" y="1" width="2.5" height="12" fill="#6d6d6d"/></svg>Trending</div>
      <div class="tab"><svg width="14" height="14" viewBox="0 0 14 14"><circle cx="7" cy="7" r="6.5" fill="#6d6d6d"/><path d="M7 3v4h3" stroke="#fff" stroke-width="1.2" fill="none"/></svg>Time Line</div>
      <div class="tab tab--active"><svg width="14" height="14" viewBox="0 0 14 14"><circle cx="7" cy="4" r="3.5" fill="#6d6d6d"/><path d="M0 14a7 6 0 0 1 14 0z" fill="#6d6d6d"/></svg>Account</div>
    </nav>
  </section>

</div>
</body>
</html>
```